Packaging Design Project

To design a universal giftbox(retail packaging) for our binoculars/optical product range. Our binoculars are in good quality and yet in affordable prices. We would like this range to be professional looking consumer products.
I have uploaded a dieline of one of the landscape boxes. We would like to see how the design looks portrait/larger boxes as well.

Specification sample: (as in file 2)

#582K (Krestholm 8X18)
Magnification: 8X
Objective: 18mm
Field Angle: 4.5°
Features: Fast Center Focusing System
Diopter and PD adjustment

#358 (Krestholm 7X18)
Magnification: 7X
Objective: 18mm
Field Angle: 4.5°
Diopter and PD adjustment

Target Market(s)

Sports/Theater/Nature

Industry/Entity Type

Landscape

Requirements
Must have
• To include our Krestholm logo.
Include the specification of the binoculars.
Nice to have
• Simple design, easy to read
Should not have
• Should not have cartoon

```html
<!DOCTYPE html>
<html lang="en">
<head>
<meta charset="utf-8">
<title>Krestholm #582K Binocular Giftbox Dieline</title>
<link href="https://fonts.googleapis.com/css2?family=Open+Sans:wght@400;600;700&family=Tinos:wght@400;700&display=swap" rel="stylesheet">
<style>
  :root {
    --bg: #c9cacc;
    --bg-light: #e6e7e9;
    --blue-deep: #1c67a8;
    --blue-mid: #3f8bcd;
    --blue-pale: #8ec6ee;
    --blue-brand: #2a78b6;
    --ink: #111111;
    --navy: #0f2a52;
    --white: #ffffff;
    --side-dark: #050505;
    --side-slate: #4c6270;
    --photo-light: #e9ecef;
    --photo-dark: #5a5f66;
  }
  html, body {
    margin: 0;
    padding: 0;
    width: 1200px;
    height: 788px;
    overflow: hidden;
    background: linear-gradient(160deg, var(--bg-light), var(--bg));
  }
  .dieline { display: block; width: 1200px; height: 788px; }
  .brand { font-family: "Open Sans", sans-serif; font-weight: 400; fill: var(--blue-brand); }
  .model { font-family: "Tinos", serif; font-weight: 700; fill: var(--ink); }
  .model-sub { font-family: "Tinos", serif; font-weight: 700; fill: var(--ink); }
  .model-light { fill: var(--white); }
  .spec { font-family: "Open Sans", sans-serif; font-weight: 700; font-size: 11.5px; fill: var(--ink); }
  .feature { font-family: "Open Sans", sans-serif; font-weight: 400; fill: var(--white); }
  .feature-title { font-size: 15px; }
  .feature-line { font-size: 12.5px; }
</style>
</head>
<body>
<svg class="dieline" viewBox="0 0 1190 781" preserveAspectRatio="none" xmlns="http://www.w3.org/2000/svg">
  <defs>
    <linearGradient id="side-panel-left" x1="0" y1="1" x2="1" y2="0">
      <stop offset="0.2" stop-color="var(--side-dark)"/>
      <stop offset="1" stop-color="var(--side-slate)"/>
    </linearGradient>
    <linearGradient id="side-panel-right" x1="0" y1="0" x2="1" y2="0">
      <stop offset="0" stop-color="var(--side-dark)"/>
      <stop offset="1" stop-color="var(--side-slate)"/>
    </linearGradient>
    <linearGradient id="glue-flap" x1="0" y1="0" x2="1" y2="0">
      <stop offset="0" stop-color="var(--blue-deep)"/>
      <stop offset="1" stop-color="var(--blue-pale)"/>
    </linearGradient>
    <linearGradient id="badge-ring" x1="0" y1="0" x2="1" y2="1">
      <stop offset="0" stop-color="var(--blue-deep)"/>
      <stop offset="1" stop-color="var(--blue-pale)"/>
    </linearGradient>
    <radialGradient id="product-photo" cx="0.4" cy="0.45" r="0.7">
      <stop offset="0" stop-color="var(--photo-light)"/>
      <stop offset="1" stop-color="var(--photo-dark)"/>
    </radialGradient>
  </defs>

  <!-- glue flap -->
  <path class="glue-flap" d="M112,268 L112,568 L70,555 Q66,553 66,548 L66,288 Q66,282 70,280 Z" fill="url(#glue-flap)"/>

  <!-- back panel with tuck lid -->
  <g class="back-lid">
    <path d="M112,268 L112,60 Q112,45 127,45 L425,45 Q440,45 440,60 L440,268 Z" fill="var(--white)"/>
    <path d="M112,92 L112,60 Q112,45 127,45 L425,45 Q440,45 440,60 L440,92 Z" fill="var(--blue-deep)"/>
    <text class="brand" x="278" y="178" font-size="34" text-anchor="middle" transform="rotate(180 278 178)">krestholm</text>
  </g>
  <path class="back-bottom-flap" d="M112,568 L440,568 L440,695 Q440,705 430,705 L380,705 Q370,705 370,695 L370,665 Q370,658 362,658 L176,658 Q168,658 168,665 L168,695 Q168,705 158,705 L122,705 Q112,705 112,695 Z" fill="var(--blue-pale)"/>

  <g class="back-panel">
    <rect x="112" y="268" width="328" height="300" fill="var(--white)"/>
    <text class="brand" x="119" y="300" font-size="29">krestholm</text>
    <g class="badge">
      <rect x="182" y="340" width="246" height="160" rx="80" fill="url(#badge-ring)"/>
      <rect x="228" y="298" width="154" height="248" rx="74" fill="url(#badge-ring)"/>
      <rect x="198" y="360" width="214" height="124" rx="60" fill="var(--white)"/>
      <rect x="246" y="316" width="118" height="212" rx="56" fill="var(--white)"/>
    </g>
    <g role="img" aria-label="Photo of silver compact binoculars">
      <rect x="232" y="362" width="146" height="102" rx="40" fill="url(#product-photo)"/>
    </g>
    <text class="model" x="305" y="500" font-size="24" text-anchor="middle" fill="var(--navy)">#582K</text>
    <text class="model-sub" x="305" y="513" font-size="9.5" text-anchor="middle" fill="var(--blue-deep)">(Krestholm 8X18)</text>
    <text class="spec" x="119" y="522">Magnification: 8X</text>
    <text class="spec" x="119" y="538">Objective: 18mm</text>
    <text class="spec" x="119" y="554">Field Angle: 4.5°</text>
  </g>

  <!-- left side panel -->
  <path class="side-top-flap" d="M440,133 L588,133 L612,210 L612,268 L440,268 Z" fill="var(--blue-deep)"/>
  <path class="side-bottom-flap" d="M440,568 L612,568 L612,695 L515,695 Q505,695 505,685 Q505,650 470,645 L440,640 Z" fill="var(--blue-deep)"/>
  <g class="side-panel">
    <rect x="440" y="268" width="172" height="300" fill="url(#side-panel-left)"/>
    <g role="img" aria-label="Small photo of silver compact binoculars">
      <rect x="455" y="288" width="80" height="48" rx="20" fill="url(#product-photo)"/>
    </g>
    <text class="model model-light" x="543" y="312" font-size="14">#582K</text>
    <text class="model-sub model-light" x="545" y="324" font-size="6.5">(Krestholm 8X18)</text>
    <text class="brand" font-size="30" transform="translate(512 515) rotate(-90)" fill="var(--blue-mid)">krestholm</text>
    <text class="feature feature-title" transform="translate(535 490) rotate(-90)">Features:</text>
    <text class="feature feature-line" transform="translate(552 552) rotate(-90)">Fast Center Focusing System</text>
    <text class="feature feature-line" transform="translate(569 546) rotate(-90)">Diopter and PD adjustment</text>
  </g>

  <!-- front panel -->
  <rect class="front-top-flap" x="612" y="115" width="330" height="153" fill="var(--blue-pale)"/>
  <path class="front-bottom-flap" d="M612,568 L942,568 L942,592 L880,655 Q872,662 872,672 L872,695 Q872,705 862,705 L698,705 Q688,705 688,695 L688,672 Q688,662 680,655 L612,592 Z" fill="var(--blue-pale)"/>
  <g class="front-panel">
    <rect x="612" y="268" width="330" height="300" fill="var(--white)"/>
    <path d="M612,432 C700,395 790,458 862,410 C905,380 915,328 942,316 L942,568 L612,568 Z" fill="var(--blue-deep)"/>
    <path d="M612,446 C700,409 795,472 868,424 C910,394 922,344 942,334 L942,568 L612,568 Z" fill="var(--blue-pale)"/>
    <text class="brand" x="908" y="313" font-size="31" text-anchor="end">krestholm</text>
    <g role="img" aria-label="Photo of silver compact binoculars">
      <rect x="632" y="330" width="208" height="142" rx="56" fill="url(#product-photo)"/>
    </g>
    <text class="model" x="700" y="528" font-size="42" text-anchor="middle">#582K</text>
    <text class="model-sub" x="700" y="548" font-size="15" text-anchor="middle">(Krestholm 8X18)</text>
    <text class="spec" x="800" y="510">Magnification: 8X</text>
    <text class="spec" x="800" y="525">Objective: 18mm</text>
    <text class="spec" x="800" y="540">Field Angle: 4.5°</text>
  </g>

  <!-- right side panel -->
  <path class="side-top-flap" d="M942,268 L942,205 L970,133 L1118,133 L1118,268 Z" fill="var(--blue-deep)"/>
  <path class="side-bottom-flap" d="M942,568 L1118,568 L1118,575 L1062,640 Q1055,648 1055,660 L1055,695 L952,695 Q942,695 942,685 Z" fill="var(--blue-deep)"/>
  <g class="side-panel">
    <rect x="942" y="268" width="176" height="300" fill="url(#side-panel-right)"/>
    <text class="brand" font-size="30" transform="translate(1014 485) rotate(-90)" fill="var(--blue-mid)">krestholm</text>
    <text class="feature feature-title" transform="translate(1050 445) rotate(-90)">Features:</text>
    <text class="feature feature-line" transform="translate(1066 510) rotate(-90)">Fast Center Focusing System</text>
    <text class="feature feature-line" transform="translate(1083 505) rotate(-90)">Diopter and PD adjustment</text>
  </g>
</svg>
</body>
</html>
```